Update New Business Card - For Start Up

I need to update my business card, I have our old version for example. I would like to keep to the same colors and theme. We are a threat reporting and case management tool for corporations and educational institutions.

Target Market(s)

Corporate Security and Human Resources, School Administrators and Superintendents.

Industry/Entity Type

Physical Security and Technology.

Contact Information for Business Card

My Name, Founder/CEO, phone number 777-412-5068, Logo, Web...

Colors
0054AA
0677BA
7BADD7
CADEEF
E8F1F8

Requirements
Must have
• Something new and trendy.

```html
<!DOCTYPE html>
<html lang="en">
<head>
<meta charset="utf-8">
<title>Sentrova Business Card</title>
<link rel="stylesheet" href="https://fonts.googleapis.com/css2?family=Montserrat:wght@400;500&family=Oswald:wght@500&display=swap">
<style>
  :root {
    --stage: #262626;
    --brand-blue: #0677BA;
    --brand-deep: #0054AA;
    --card-front-a: #1f73bb;
    --card-front-b: #3384c6;
    --mark-tone: #155f9f;
    --mark-dot: #2a8fe0;
    --paper: #ffffff;
    --ink: #2b2b2b;
  }
  * { box-sizing: border-box; margin: 0; padding: 0; }
  html, body { width: 1200px; height: 900px; overflow: hidden; }
  body {
    background: var(--stage);
    display: flex;
    flex-direction: column;
    align-items: center;
    justify-content: center;
    gap: 24px;
  }
  .card {
    width: 700px;
    height: 400px;
    box-shadow: 0 8px 24px rgba(0,0,0,0.5);
  }
  .card-front {
    background: linear-gradient(120deg, var(--card-front-a), var(--card-front-b));
    display: flex;
    align-items: center;
    justify-content: center;
    gap: 22px;
  }
  .brand-dot {
    width: 96px;
    height: 96px;
    border-radius: 50%;
    background: var(--mark-dot);
  }
  .brand-name {
    font-family: "Montserrat", sans-serif;
    font-weight: 500;
    font-size: 62px;
    letter-spacing: 8px;
    text-transform: uppercase;
    color: var(--mark-tone);
  }
  .card-back {
    background: var(--paper);
    display: flex;
    align-items: center;
    justify-content: center;
    gap: 30px;
  }
  .identity { text-align: right; }
  .person-name {
    font-family: "Oswald", sans-serif;
    font-weight: 500;
    font-size: 44px;
    line-height: 1.05;
    text-transform: uppercase;
    color: var(--brand-blue);
  }
  .person-title {
    font-family: "Montserrat", sans-serif;
    font-size: 21px;
    color: var(--ink);
  }
  .divider {
    width: 2px;
    height: 78px;
    background: var(--brand-blue);
  }
  .contacts { list-style: none; }
  .contacts li {
    display: flex;
    align-items: center;
    gap: 10px;
    font-family: "Montserrat", sans-serif;
    font-size: 21px;
    line-height: 1.35;
    color: var(--ink);
  }
  .contacts svg { width: 16px; height: 16px; flex: none; }
</style>
</head>
<body>
  <section class="card card-front">
    <span class="brand-dot"></span>
    <span class="brand-name">Sentrova</span>
  </section>

  <section class="card card-back">
    <div class="identity">
      <h1 class="person-name">Dana Kessler</h1>
      <p class="person-title">Founder/CEO</p>
    </div>
    <span class="divider"></span>
    <ul class="contacts">
      <li>
        <svg viewBox="0 0 16 16" aria-hidden="true"><path d="M4 1l3 3-1.6 1.8a9 9 0 0 0 4.8 4.8L12 9l3 3-2 2.5C7 14 2 9 1.5 3z" fill="var(--brand-blue)"/></svg>
        777-412-5068
      </li>
      <li>
        <svg viewBox="0 0 16 16" aria-hidden="true"><rect x="1.5" y="3.5" width="13" height="9" fill="none" stroke="var(--brand-blue)" stroke-width="1.6"/><path d="M1.5 3.5l6.5 5 6.5-5" fill="none" stroke="var(--brand-blue)" stroke-width="1.6"/></svg>
        dana@sentrova.co
      </li>
      <li>
        <svg viewBox="0 0 16 16" aria-hidden="true"><g fill="none" stroke="var(--brand-blue)" stroke-width="1.3"><circle cx="8" cy="8" r="6.5"/><ellipse cx="8" cy="8" rx="3" ry="6.5"/><path d="M1.5 8h13M2.5 4.8h11M2.5 11.2h11"/></g></svg>
        www.sentrova.co
      </li>
    </ul>
  </section>
</body>
</html>
```